依頼詳細
■依頼目的
本ブログの目的は、ミラノーヴァ テクノサービシズの認知拡大とブランディングとなります。
MTSの技術や最新動向への見解・取組を掲載する「MTS Tech ブログ」を立ち上げ、
中途採用 転職意向者 / ソリューション導入 検討者の意向を上げることを狙っております。

■デザインイメージ
ポルタリンク社運営ブログ「Buildnotes.XY」
http://dev.portalink-example.jp/
制作注意点としまして、実装にはWordPressを使いますのでWordPressで実装が明らかにできないような
デザインは避けてください

■訴求ポイントの優先順位
1.ブログスペース
2.求人広告バナーエリア(自社のキャリア採用)

■ターゲット層
個人:中途採用 転職意向者
法人:ソリューション導入 検討者

■希望する色味
ミラノーヴァテクノサービシズのトーン&マナーに合わせたもの
http://www.mts.mirano-example.co.jp/

■提供素材
ミラノーヴァテクノサービシズ:ロゴデーター

■納品ファイル
TOPページデザイン1点(PSDデータ)
ロゴの使用につきましては、添付のレギュレーションに従って作成をお願い致します。
デザインコンセプトにつきまして補足をさせて頂きます。TOPページのイメージとしまして一般的なブログ形式ではなく、デザインとレイアウトに関しましては最近のビジネスブログやキュレーションメディアのトレンドも考慮した先進性のあるデザインを考慮し、なおかつ読みやすい体裁での設計をお願いいたします。皆様からのご提案を心よりお待ちしております。よろしくお願いいたします。
ランサー様各位
この度は、たくさんの素晴らしいご提案を頂きましてありがとうございます。
さらにより多くの方からの魅力的なご応募を頂けるのではと思いまして
一週間延長の3/11(水)に延長することといたしました。
引き続き皆様からのご提案をお待ち申し上げます。

サイトの性質上、どうしても縦に長くなる中で、背景色に変化をつけることにより、情報ごとのブロックの認識がわかりやすくなったと感じます。また、単純なグリッドデザインでなくなり、変化がついていたところが決定したポイントになります。

この度は、皆様に当コンペにたくさんの素晴らしいデザインをご提案して頂きましてありがとうございました。

```html
<!DOCTYPE html>
<html lang="ja">
<head>
<meta charset="utf-8">
<title>MTS Tech ブログ</title>
<link rel="stylesheet" href="https://fonts.googleapis.com/css2?family=Noto+Sans+JP:wght@400;500;700;900&display=swap">
<style>
:root{
  --navy:#0f2350;
  --blue:#1d4f9c;
  --link:#1a3f7a;
  --accent:#2a8ad9;
  --page:#e8ebf0;
  --panel:#f4f5f8;
  --white:#ffffff;
  --text:#222a36;
  --muted:#7a8494;
  --line:#d5dae2;
  --gold:#f2c12e;
}
*{box-sizing:border-box;margin:0;padding:0}
html,body{width:1200px;height:2180px;overflow:hidden}
body{background:var(--page);font-family:"Noto Sans JP",sans-serif;color:var(--text);position:relative;font-size:12px}
ul{list-style:none}

.site-header{position:absolute;left:0;top:0;width:1200px;height:110px;background:var(--white);border-bottom:3px solid var(--navy)}
.site-title{position:absolute;left:40px;top:32px;font-size:30px;font-weight:700;color:var(--blue);letter-spacing:1px}
.site-title small{font-size:22px;color:var(--navy);margin-left:6px}
.brand-block{position:absolute;left:470px;top:0;width:260px;height:107px;background:var(--navy);display:flex;align-items:center;justify-content:center;gap:10px}
.brand-block .mark{width:18px;height:18px;background:var(--white)}
.brand-block .name{color:var(--white);font-size:18px;font-weight:700;line-height:1.2}
.brand-block .name span{display:block;font-size:11px;font-weight:400}
.search{position:absolute;right:40px;top:38px;width:240px;height:32px;display:flex}
.search .field{flex:1;background:var(--navy);color:#b8c3d8;font-size:12px;padding:7px 10px}
.search .btn{width:32px;background:var(--blue);display:flex;align-items:center;justify-content:center}

.side-nav{position:absolute;left:40px;top:130px;width:185px}
.side-nav li{height:32px;line-height:32px;padding-left:12px;border-bottom:1px solid var(--line);font-size:13px;color:var(--link);background:var(--panel)}
.side-nav li.active{background:var(--blue);color:var(--white);font-weight:700}

.main{position:absolute;left:238px;top:130px;width:566px;background:var(--white);padding:14px 16px 10px}
.section-head{font-size:14px;font-weight:700;color:var(--navy);border-left:4px solid var(--blue);padding-left:8px;margin-bottom:12px;line-height:20px}
.featured{display:flex;gap:16px;padding-bottom:14px;border-bottom:1px solid var(--line)}
.thumb{flex:none;background:linear-gradient(135deg,#2c3d55,#8aa0b8 55%,#1a2433)}
.thumb.green{background:linear-gradient(135deg,#0a1a0e,#2a8a3a 50%,#0d2a12)}
.thumb.dusk{background:radial-gradient(circle at 50% 70%,#e8eef8,#4a6488 45%,#0e1a30)}
.thumb.sky{background:linear-gradient(135deg,#5bb8ef,#2a8ad9)}
.featured .thumb{width:250px;height:170px}
.featured h2{font-size:18px;line-height:1.45;color:var(--navy);font-weight:700;margin-bottom:10px}
.excerpt{font-size:11px;color:#4c5666;line-height:1.6}
.meta{display:flex;gap:12px;font-size:10px;color:var(--muted);margin-top:8px}
.meta .cat{color:var(--accent)}

.post{display:flex;gap:14px;padding:10px 0;border-bottom:1px solid var(--line);height:86px}
.post .thumb{width:100px;height:66px}
.post h3{font-size:14px;color:var(--link);font-weight:700;line-height:1.3;margin-bottom:4px}
.post .excerpt{font-size:10.5px;line-height:1.5}
.post .meta{margin-top:3px}

.career-banner{margin:14px 0;height:200px;background:#f7f8fa;border:1px solid var(--line);display:flex}
.career-banner .copy{flex:1;padding:26px 22px}
.career-banner .big{font-size:36px;font-weight:900;color:#111;line-height:1.25}
.career-banner .big em{font-style:normal;color:var(--blue)}
.career-banner .sub{font-size:11px;color:#444;margin-top:12px;line-height:1.5}
.career-banner .photo{width:210px;background:linear-gradient(160deg,#ffffff,#c9d0da 60%,#3a4452)}

.sidebar{position:absolute;left:822px;top:130px;width:338px}
.ad-banner{height:300px;background:var(--navy);display:flex;flex-direction:column}
.ad-banner .top{flex:1;display:flex}
.ad-banner .person{width:120px;background:linear-gradient(180deg,#2a3c66,#6f7fa0)}
.ad-banner .words{flex:1;padding:18px 14px;color:var(--white);font-size:26px;font-weight:900;line-height:1.32;text-align:right}
.ad-banner .words .hot{color:var(--gold)}
.ad-banner .bottom{height:52px;background:var(--white);display:flex;align-items:center;justify-content:space-between;padding:0 14px;border:2px solid var(--navy)}
.ad-banner .bottom .tag{font-size:13px;font-weight:700;color:var(--navy)}
.ad-banner .bottom .logo{display:flex;align-items:center;gap:6px;background:var(--navy);color:var(--white);font-size:11px;font-weight:700;padding:6px 8px}
.ad-banner .bottom .logo i{width:10px;height:10px;background:var(--white)}

.widget{background:var(--panel);margin-top:16px;padding:12px 12px 10px}
.widget .section-head{margin-bottom:10px}
.rank{display:flex;gap:10px;padding:7px 0;border-bottom:1px solid var(--line)}
.rank .thumb{width:62px;height:50px}
.rank h4{font-size:12px;color:var(--link);font-weight:700;line-height:1.4}
.rank .meta{margin-top:3px}
.tags{display:flex;flex-wrap:wrap;gap:6px}
.tags span{background:var(--white);border:1px solid var(--line);font-size:11px;padding:4px 10px;color:var(--link)}
.calendar{width:100%;border-collapse:collapse;background:var(--white);font-size:11px;text-align:center}
.calendar caption{font-size:12px;font-weight:700;color:var(--navy);padding:4px 0 6px}
.calendar th{background:var(--blue);color:var(--white);font-weight:500;padding:5px 0}
.calendar td{border:1px solid var(--line);padding:6px 0;color:#444}
.calendar td.has{color:var(--accent);font-weight:700}

.site-footer{position:absolute;left:0;top:2010px;width:1200px;height:170px;background:var(--white);border-top:3px solid var(--navy)}
.footer-brand{position:absolute;left:40px;top:40px;display:flex;align-items:center;gap:8px}
.footer-brand i{width:16px;height:16px;background:var(--navy)}
.footer-brand b{font-size:18px;color:var(--navy)}
.footer-brand span{display:block;font-size:10px;font-weight:400}
.footer-links{position:absolute;left:260px;top:50px;font-size:12px;color:var(--link)}
.footer-social{position:absolute;right:40px;top:42px;display:flex;gap:10px}
.footer-social i{width:30px;height:30px;background:var(--blue)}
.footer-social i+i{background:var(--accent)}
.copyright{position:absolute;left:0;right:0;top:120px;text-align:center;font-size:10px;color:var(--muted)}
</style>
</head>
<body>

<header class="site-header">
  <div class="site-title">MTS<small>Tech ブログ</small></div>
  <div class="brand-block"><i class="mark"></i><div class="name">Milanova<span>Techno Services</span></div></div>
  <div class="search">
    <div class="field">キーワードを入力</div>
    <div class="btn"><svg width="16" height="16" viewBox="0 0 16 16"><circle cx="7" cy="7" r="5" fill="none" stroke="#fff" stroke-width="2"/><line x1="11" y1="11" x2="15" y2="15" stroke="#fff" stroke-width="2"/></svg></div>
  </div>
</header>

<nav class="side-nav">
  <ul>
    <li class="active">トップページ</li>
    <li>コラム</li>
    <li>Chirpline</li>
    <li>QueryKit</li>
    <li>Javelin</li>
    <li>ビジネスモデル</li>
    <li>PocketOS</li>
    <li>HTML5</li>
    <li>CSS3</li>
    <li>Ruby</li>
    <li>Database</li>
    <li>Paneo Phone</li>
  </ul>
</nav>

<main class="main">
  <h1 class="section-head">最新の記事</h1>
  <article class="featured">
    <div class="thumb" role="img" aria-label="夕暮れの高層ビル街の写真"></div>
    <div>
      <h2>ミラノーヴァ テクノサービシズの新規メディア</h2>
      <p class="excerpt">MTSのクラウドサービスとソリューションを活用することで、業務に最適なシステムをスピーディに提供します。</p>
      <div class="meta"><span>2015.03.01</span><span class="cat">ビジネスモデル</span><span>1250 views</span></div>
    </div>
  </article>

  <article class="post"><div class="thumb green" role="img" aria-label="緑のデジタル文字が並ぶ画面の写真"></div><div><h3>ミラノーヴァ テクノサービシズの新規メディア</h3><p class="excerpt">MTSのクラウドサービスとソリューションを活用することで、業務に最適なシステムを提供します。</p><div class="meta"><span>2015.03.01</span><span class="cat">コラム</span><span>980 views</span></div></div></article>
  <article class="post"><div class="thumb" role="img" aria-label="高層ビル街の写真"></div><div><h3>ミラノーヴァ テクノサービシズの新規メディア</h3><p class="excerpt">MTSのクラウドサービスとソリューションを活用することで、業務に最適なシステムを提供します。</p><div class="meta"><span>2015.02.28</span><span class="cat">HTML5</span><span>860 views</span></div></div></article>
  <article class="post"><div class="thumb green" role="img" aria-label="緑のデジタル文字が並ぶ画面の写真"></div><div><h3>ミラノーヴァ テクノサービシズの新規メディア</h3><p class="excerpt">MTSのクラウドサービスとソリューションを活用することで、業務に最適なシステムを提供します。</p><div class="meta"><span>2015.02.27</span><span class="cat">Database</span><span>740 views</span></div></div></article>
  <article class="post"><div class="thumb dusk" role="img" aria-label="光が差す地平線の写真"></div><div><h3>ミラノーヴァ テクノサービシズの新規メディア</h3><p class="excerpt">MTSのクラウドサービスとソリューションを活用することで、業務に最適なシステムを提供します。</p><div class="meta"><span>2015.02.26</span><span class="cat">CSS3</span><span>690 views</span></div></div></article>

  <aside class="career-banner">
    <div class="copy">
      <p class="big">年収<em>800万円</em>以上の求人と<br>非公開求人</p>
      <p class="sub">MTSのキャリア採用では、専門性を活かせる<br>ポジションを多数ご用意しています。</p>
    </div>
    <div class="photo" role="img" aria-label="書類とペンが置かれた机の写真"></div>
  </aside>

  <article class="post"><div class="thumb dusk" role="img" aria-label="光が差す地平線の写真"></div><div><h3>ミラノーヴァ テクノサービシズの新規メディア</h3><p class="excerpt">MTSのクラウドサービスとソリューションを活用することで、業務に最適なシステムを提供します。</p><div class="meta"><span>2015.02.25</span><span class="cat">Ruby</span><span>620 views</span></div></div></article>
  <article class="post"><div class="thumb green" role="img" aria-label="緑のデジタル文字が並ぶ画面の写真"></div><div><h3>ミラノーヴァ テクノサービシズの新規メディア</h3><p class="excerpt">MTSのクラウドサービスとソリューションを活用することで、業務に最適なシステムを提供します。</p><div class="meta"><span>2015.02.24</span><span class="cat">Javelin</span><span>580 views</span></div></div></article>
  <article class="post"><div class="thumb" role="img" aria-label="高層ビル街の写真"></div><div><h3>ミラノーヴァ テクノサービシズの新規メディア</h3><p class="excerpt">MTSのクラウドサービスとソリューションを活用することで、業務に最適なシステムを提供します。</p><div class="meta"><span>2015.02.23</span><span class="cat">コラム</span><span>540 views</span></div></div></article>
  <article class="post"><div class="thumb dusk" role="img" aria-label="光が差す地平線の写真"></div><div><h3>ミラノーヴァ テクノサービシズの新規メディア</h3><p class="excerpt">MTSのクラウドサービスとソリューションを活用することで、業務に最適なシステムを提供します。</p><div class="meta"><span>2015.02.22</span><span class="cat">HTML5</span><span>510 views</span></div></div></article>
  <article class="post"><div class="thumb green" role="img" aria-label="緑のデジタル文字が並ぶ画面の写真"></div><div><h3>ミラノーヴァ テクノサービシズの新規メディア</h3><p class="excerpt">MTSのクラウドサービスとソリューションを活用することで、業務に最適なシステムを提供します。</p><div class="meta"><span>2015.02.21</span><span class="cat">PocketOS</span><span>470 views</span></div></div></article>
  <article class="post"><div class="thumb" role="img" aria-label="高層ビル街の写真"></div><div><h3>ミラノーヴァ テクノサービシズの新規メディア</h3><p class="excerpt">MTSのクラウドサービスとソリューションを活用することで、業務に最適なシステムを提供します。</p><div class="meta"><span>2015.02.20</span><span class="cat">Database</span><span>440 views</span></div></div></article>
  <article class="post"><div class="thumb dusk" role="img" aria-label="光が差す地平線の写真"></div><div><h3>ミラノーヴァ テクノサービシズの新規メディア</h3><p class="excerpt">MTSのクラウドサービスとソリューションを活用することで、業務に最適なシステムを提供します。</p><div class="meta"><span>2015.02.19</span><span class="cat">CSS3</span><span>410 views</span></div></div></article>
  <article class="post"><div class="thumb green" role="img" aria-label="緑のデジタル文字が並ぶ画面の写真"></div><div><h3>ミラノーヴァ テクノサービシズの新規メディア</h3><p class="excerpt">MTSのクラウドサービスとソリューションを活用することで、業務に最適なシステムを提供します。</p><div class="meta"><span>2015.02.18</span><span class="cat">コラム</span><span>380 views</span></div></div></article>
  <article class="post"><div class="thumb" role="img" aria-label="高層ビル街の写真"></div><div><h3>ミラノーヴァ テクノサービシズの新規メディア</h3><p class="excerpt">MTSのクラウドサービスとソリューションを活用することで、業務に最適なシステムを提供します。</p><div class="meta"><span>2015.02.17</span><span class="cat">Ruby</span><span>350 views</span></div></div></article>
  <article class="post"><div class="thumb dusk" role="img" aria-label="光が差す地平線の写真"></div><div><h3>ミラノーヴァ テクノサービシズの新規メディア</h3><p class="excerpt">MTSのクラウドサービスとソリューションを活用することで、業務に最適なシステムを提供します。</p><div class="meta"><span>2015.02.16</span><span class="cat">HTML5</span><span>320 views</span></div></div></article>
  <article class="post"><div class="thumb green" role="img" aria-label="緑のデジタル文字が並ぶ画面の写真"></div><div><h3>ミラノーヴァ テクノサービシズの新規メディア</h3><p class="excerpt">MTSのクラウドサービスとソリューションを活用することで、業務に最適なシステムを提供します。</p><div class="meta"><span>2015.02.15</span><span class="cat">Javelin</span><span>300 views</span></div></div></article>
</main>

<aside class="sidebar">
  <div class="ad-banner">
    <div class="top">
      <div class="person" role="img" aria-label="スーツ姿のビジネスパーソンの写真"></div>
      <div class="words">コンサル<br>PMO<br>デジタルマーケ<br>ERP<br><span class="hot">高額案件多数</span></div>
    </div>
    <div class="bottom"><span class="tag">ミラノーヴァ フリーランス支援</span><span class="logo"><i></i>Milanova</span></div>
  </div>

  <section class="widget">
    <h2 class="section-head">Weeklyランキング</h2>
    <div class="rank"><div class="thumb sky" role="img" aria-label="記事のサムネイル画像"></div><div><h4>ミラノーヴァ テクノサービシズの新規メディア</h4><div class="meta"><span class="cat">コラム</span><span>2350 views</span></div></div></div>
    <div class="rank"><div class="thumb sky" role="img" aria-label="記事のサムネイル画像"></div><div><h4>ミラノーヴァ テクノサービシズの新規メディア</h4><div class="meta"><span class="cat">HTML5</span><span>2120 views</span></div></div></div>
    <div class="rank"><div class="thumb sky" role="img" aria-label="記事のサムネイル画像"></div><div><h4>ミラノーヴァ テクノサービシズの新規メディア</h4><div class="meta"><span class="cat">Ruby</span><span>1980 views</span></div></div></div>
    <div class="rank"><div class="thumb sky" role="img" aria-label="記事のサムネイル画像"></div><div><h4>ミラノーヴァ テクノサービシズの新規メディア</h4><div class="meta"><span class="cat">CSS3</span><span>1760 views</span></div></div></div>
    <div class="rank"><div class="thumb sky" role="img" aria-label="記事のサムネイル画像"></div><div><h4>ミラノーヴァ テクノサービシズの新規メディア</h4><div class="meta"><span class="cat">Database</span><span>1540 views</span></div></div></div>
  </section>

  <section class="widget">
    <h2 class="section-head">今週のBESTキーワード</h2>
    <div class="tags"><span>ビジネスソリューション</span><span>クラウド</span><span>セキュリティ</span><span>HTML5</span><span>データ分析</span></div>
  </section>

  <section class="widget">
    <h2 class="section-head">アーカイブ</h2>
    <table class="calendar">
      <caption>2015年 3月</caption>
      <tr><th>日</th><th>月</th><th>火</th><th>水</th><th>木</th><th>金</th><th>土</th></tr>
      <tr><td class="has">1</td><td>2</td><td>3</td><td>4</td><td>5</td><td>6</td><td>7</td></tr>
      <tr><td>8</td><td>9</td><td class="has">10</td><td>11</td><td>12</td><td>13</td><td>14</td></tr>
      <tr><td>15</td><td>16</td><td>17</td><td>18</td><td>19</td><td>20</td><td>21</td></tr>
      <tr><td>22</td><td>23</td><td>24</td><td>25</td><td>26</td><td>27</td><td>28</td></tr>
      <tr><td>29</td><td>30</td><td>31</td><td></td><td></td><td></td><td></td></tr>
    </table>
  </section>

  <section class="widget">
    <h2 class="section-head">最新ランキング</h2>
    <div class="rank"><div class="thumb sky" role="img" aria-label="記事のサムネイル画像"></div><div><h4>ミラノーヴァ テクノサービシズの新規メディア</h4><div class="meta"><span class="cat">コラム</span><span>1320 views</span></div></div></div>
    <div class="rank"><div class="thumb sky" role="img" aria-label="記事のサムネイル画像"></div><div><h4>ミラノーヴァ テクノサービシズの新規メディア</h4><div class="meta"><span class="cat">Javelin</span><span>1180 views</span></div></div></div>
    <div class="rank"><div class="thumb sky" role="img" aria-label="記事のサムネイル画像"></div><div><h4>ミラノーヴァ テクノサービシズの新規メディア</h4><div class="meta"><span class="cat">HTML5</span><span>1050 views</span></div></div></div>
    <div class="rank"><div class="thumb sky" role="img" aria-label="記事のサムネイル画像"></div><div><h4>ミラノーヴァ テクノサービシズの新規メディア</h4><div class="meta"><span class="cat">CSS3</span><span>940 views</span></div></div></div>
    <div class="rank"><div class="thumb sky" role="img" aria-label="記事のサムネイル画像"></div><div><h4>ミラノーヴァ テクノサービシズの新規メディア</h4><div class="meta"><span class="cat">Ruby</span><span>870 views</span></div></div></div>
  </section>
</aside>

<footer class="site-footer">
  <div class="footer-brand"><i></i><b>Milanova<span>Techno Services</span></b></div>
  <div class="footer-links">about ｜ 利用規約</div>
  <div class="footer-social"><i></i><i></i></div>
  <p class="copyright">©Milanova Techno Services Inc.</p>
</footer>

</body>
</html>
```